Looking for a high-end business card design for a construction company

We are looking to update our business card design. We are a post-frame construction company that builds custom buildings, commercial spaces, homes, and anything else. We have multiple people working here so we would need something we can easily customize the information for the specific person. We need a name, website, cell phone, office phone as well as social icons. Our colors are black, white, and grey/silver so I would love a black background or something that is more striking than just a traditional white business card. Looking for something that is very professional with a high-end look/feel. I have attached our logos, they can be silver, white, grey, or black.
Industry/Entity Type
Construction
Contact Information for Business Card
Business logo, Name, Cell phone, Office phone, website, social Icons
Colors
Designer to choose only greyscale colors for use in the design.
Look and feel

```html
<!DOCTYPE html>
<html lang="en">
<head>
<meta charset="utf-8">
<title>Kestrel Builders, Inc. — Business Card</title>
<link href="https://fonts.googleapis.com/css2?family=Arimo:wght@400;700&display=swap" rel="stylesheet">
<style>
  :root {
    --backdrop: #e6e6e4;
    --paper: #f7f7f5;
    --ink: #1c1c1c;
    --ink-soft: #2e2e2e;
    --rule: #3a3a3a;
    --card-dark: #232325;
    --card-dark-deep: #161617;
    --silver: #ececec;
  }
  * { box-sizing: border-box; margin: 0; padding: 0; }
  html, body {
    width: 1200px; height: 801px; overflow: hidden;
    background: var(--backdrop);
    font-family: "Arimo", Arial, sans-serif;
  }
  .stage {
    position: relative; width: 1200px; height: 801px;
    display: flex; align-items: center; justify-content: center; gap: 40px;
  }
  .card {
    position: relative; width: 540px; height: 309px;
    box-shadow: 0 10px 24px rgba(0,0,0,0.18);
  }
  /* front */
  .card-front { background: var(--paper); color: var(--ink); }
  .brand {
    position: absolute; top: 48px; left: 0; right: 0;
    display: flex; align-items: center; justify-content: center; gap: 12px;
  }
  .brand-dot { width: 14px; height: 14px; border-radius: 50%; background: var(--ink); }
  .brand-name {
    font-weight: 700; font-size: 20px; letter-spacing: 3px; line-height: 1.05;
    text-transform: uppercase;
  }
  .brand-name span { display: block; font-size: 12px; letter-spacing: 2.6px; }
  .person {
    position: absolute; left: 40px; top: 140px;
  }
  .person-name { font-weight: 700; font-size: 17px; letter-spacing: 0.3px; text-transform: uppercase; }
  .person-role { font-size: 13px; color: var(--ink-soft); margin-top: 2px; }
  .divider {
    position: absolute; left: 40px; right: 40px; top: 186px;
    height: 1px; background: var(--rule);
  }
  .contacts { position: absolute; left: 40px; top: 202px; list-style: none; }
  .contacts li {
    display: flex; align-items: center; gap: 9px;
    font-size: 13.5px; line-height: 22px; color: var(--ink);
  }
  .contacts svg { width: 11px; height: 11px; fill: var(--ink); flex: none; }
  .address {
    position: absolute; right: 40px; top: 202px; text-align: right;
    font-size: 13.5px; line-height: 20px; color: var(--ink-soft);
  }
  /* back */
  .card-back {
    background: radial-gradient(ellipse at 62% 38%, #3a3a3c 0%, var(--card-dark) 45%, var(--card-dark-deep) 100%);
    color: var(--silver);
  }
  .back-brand {
    position: absolute; left: 0; right: 0; bottom: 56px; text-align: center;
    font-weight: 700; text-transform: uppercase; line-height: 1.05;
  }
  .back-brand-main { font-size: 40px; letter-spacing: 7px; }
  .back-brand-sub { font-size: 22px; letter-spacing: 5px; }
</style>
</head>
<body>
<main class="stage">
  <section class="card card-front" aria-label="Business card front">
    <div class="brand">
      <span class="brand-dot"></span>
      <div class="brand-name">Kestrel<span>Builders, Inc.</span></div>
    </div>
    <div class="person">
      <div class="person-name">Daniel Reyes</div>
      <div class="person-role">Manager</div>
    </div>
    <div class="divider"></div>
    <ul class="contacts">
      <li><svg viewBox="0 0 24 24"><path d="M6.6 10.8a15 15 0 0 0 6.6 6.6l2.2-2.2a1 1 0 0 1 1-.25 11.4 11.4 0 0 0 3.6.6 1 1 0 0 1 1 1V20a1 1 0 0 1-1 1A17 17 0 0 1 3 4a1 1 0 0 1 1-1h3.5a1 1 0 0 1 1 1c0 1.25.2 2.45.6 3.6a1 1 0 0 1-.25 1z"/></svg>123-456-2100</li>
      <li><svg viewBox="0 0 24 24"><path d="M2 5h20v14H2z M2 5l10 8 10-8" fill="none" stroke="#1c1c1c" stroke-width="2.4"/><path d="M2 5h20l-10 8z"/></svg>youremail@example.com</li>
      <li><svg viewBox="0 0 24 24"><circle cx="12" cy="12" r="10" fill="none" stroke="#1c1c1c" stroke-width="2.4"/><path d="M2 12h20M12 2c3 3 3 17 0 20M12 2c-3 3-3 17 0 20" fill="none" stroke="#1c1c1c" stroke-width="2"/></svg>www.yourwebsite.com</li>
    </ul>
    <div class="address">Your address<br>city, state, ZIP 0000</div>
  </section>

  <section class="card card-back" aria-label="Business card back">
    <div class="back-brand">
      <div class="back-brand-main">Kestrel</div>
      <div class="back-brand-sub">Builders, Inc.</div>
    </div>
  </section>
</main>
</body>
</html>
```